TALBRIN ELEVATOR CORP

LOOKING FOR BLACK MATTE BACKGROUND WITH GLOSS DESIGN
NEED RAISED UV ON LOGO AND LETTERING , WITH ROUNDED CORNERS AND COLORED EDGES ( FLOURECENT BLUE)

```html
<!DOCTYPE html>
<html lang="en">
<head>
<meta charset="utf-8">
<title>Talbrin Elevator Corp – Business Card</title>
<link href="https://fonts.googleapis.com/css2?family=Poppins:wght@400;500;600&family=Tinos:wght@400&display=swap" rel="stylesheet">
<style>
  :root {
    --bg: #a9a9ab;
    --card: #1b1c1f;
    --edge: #1f8fe6;
    --accent: #2d97e8;
    --text: #e9e9ea;
    --muted: #55575c;
    --gloss-light: #d8d8da;
    --gloss-dark: #4a4b4f;
  }
  * { box-sizing: border-box; margin: 0; padding: 0; }
  html, body { width: 1200px; height: 801px; overflow: hidden; }
  body {
    background: var(--bg);
    font-family: "Poppins", Arial, sans-serif;
    position: relative;
  }
  .card {
    position: absolute;
    top: 250px;
    width: 525px;
    height: 300px;
    background: var(--card);
    border-radius: 22px;
    border: 3px solid var(--edge);
    box-shadow: 0 10px 24px rgba(0,0,0,0.28);
    overflow: hidden;
  }
  .card--front { left: 50px; }
  .card--back { left: 625px; }

  /* Front side */
  .identity {
    position: absolute;
    left: 44px;
    top: 118px;
    width: 210px;
    text-align: right;
  }
  .identity__name {
    font-weight: 600;
    font-size: 25px;
    letter-spacing: 0.5px;
    color: var(--accent);
    line-height: 1.1;
  }
  .identity__company {
    font-size: 12px;
    color: var(--text);
    margin-top: 4px;
  }
  .identity__role {
    font-size: 12px;
    color: var(--muted);
  }
  .divider {
    position: absolute;
    left: 272px;
    top: 88px;
    width: 1px;
    height: 90px;
    background: var(--accent);
  }
  .contact {
    position: absolute;
    left: 290px;
    top: 84px;
    list-style: none;
    font-size: 11.5px;
    color: var(--text);
    line-height: 1.45;
  }
  .contact li { display: flex; align-items: flex-start; gap: 8px; }
  .contact svg { width: 10px; height: 10px; margin-top: 4px; flex: none; fill: var(--accent); }
  .contact .contact__plain { padding-left: 18px; }
  .brand-mark {
    position: absolute;
    right: 26px;
    top: 26px;
    display: flex;
    align-items: center;
    gap: 6px;
    font-size: 11px;
    font-weight: 500;
    color: var(--text);
  }
  .brand-mark__dot {
    width: 14px; height: 14px; border-radius: 50%;
    background: var(--accent);
  }

  /* Back side */
  .wordmark {
    position: absolute;
    left: 48px;
    top: 105px;
    font-family: "Tinos", "Times New Roman", serif;
    text-transform: uppercase;
  }
  .wordmark__name {
    font-size: 33px;
    letter-spacing: 1px;
    background: linear-gradient(100deg, var(--gloss-light) 0%, #a8a9ad 45%, var(--gloss-dark) 100%);
    -webkit-background-clip: text;
    background-clip: text;
    color: transparent;
    white-space: nowrap;
  }
  .wordmark__row { display: flex; align-items: center; gap: 14px; margin-top: 4px; }
  .wordmark__rule {
    height: 4px;
    background: linear-gradient(90deg, var(--gloss-light), #9a9b9f);
  }
  .wordmark__rule--left { width: 100px; }
  .wordmark__rule--right { width: 80px; background: linear-gradient(90deg, #5a5b5f, #2a2b2e); }
  .wordmark__services {
    font-size: 23px;
    letter-spacing: 1px;
    color: #8e8f93;
    white-space: nowrap;
  }
</style>
</head>
<body>
  <section class="card card--front" aria-label="Business card front">
    <div class="brand-mark"><span class="brand-mark__dot"></span>TALBRIN</div>
    <div class="identity">
      <p class="identity__name">DANIEL HARTWELL</p>
      <p class="identity__company">Talbrin Elevator Corp</p>
      <p class="identity__role">President</p>
    </div>
    <div class="divider"></div>
    <ul class="contact">
      <li><svg viewBox="0 0 10 10"><path d="M5 0a3.5 3.5 0 0 0-3.5 3.5C1.5 6 5 10 5 10s3.5-4 3.5-6.5A3.5 3.5 0 0 0 5 0zm0 5a1.4 1.4 0 1 1 0-2.8A1.4 1.4 0 0 1 5 5z"/></svg><span>742 Harlan avenue</span></li>
      <li class="contact__plain">Bronx, NY 10466</li>
      <li><svg viewBox="0 0 10 10"><path d="M2 0l2 2.5-1.2 1.3a6 6 0 0 0 3.4 3.4L7.5 6 10 8 8.5 10C4 10 0 6 0 1.5z"/></svg><span>555-214-3870</span></li>
      <li><svg viewBox="0 0 10 10"><path d="M0 2h10v6H0zm1 1v.3l4 2.5 4-2.5V3z"/></svg><span>talbrinelevator@mail.com</span></li>
      <li><svg viewBox="0 0 10 10"><circle cx="5" cy="5" r="5"/></svg><span>talbrinelevatorny.com</span></li>
      <li class="contact__plain">est 1978</li>
    </ul>
  </section>

  <section class="card card--back" aria-label="Business card back">
    <div class="wordmark">
      <p class="wordmark__name">Talbrin Elevator Corp</p>
      <div class="wordmark__row">
        <span class="wordmark__rule wordmark__rule--left"></span>
        <span class="wordmark__services">Elevator Services</span>
        <span class="wordmark__rule wordmark__rule--right"></span>
      </div>
    </div>
  </section>
</body>
</html>
```